PIETRO business card - High end Italian floors and coverings

We need a new design for our business card. We are an exclusive company located in Mexico.
Our commercial name is PIETRO. Our legal name is Grande Volta SA de CV.
We bring the latest trends in materials for floors and walls such as natural stones, wood, leather, design porcelanato tiles and so.
Our company image colors are black, white and red.
Our customers are high end architects and designers.
We are looking for an elegant but fresh design which reflects exclusivity, simplicity and reliability.
(we are working also in a new website)

Requirements
Nice to have
• back and front design
Space for 2 addresses (one for each showroom location)

```html
<!DOCTYPE html>
<html lang="es">
<head>
<meta charset="utf-8">
<title>PIETRO business card</title>
<link href="https://fonts.googleapis.com/css2?family=Quicksand:wght@400;500&display=swap" rel="stylesheet">
<style>
  :root {
    --page: #e9e7e4;
    --card-white: #ffffff;
    --card-black: #0b0b0b;
    --ink: #1e1e1e;
    --red: #c8141c;
    --light: #f2f2f2;
  }
  * { margin: 0; padding: 0; box-sizing: border-box; }
  html, body { width: 1200px; height: 1000px; overflow: hidden; }
  body {
    background: var(--page);
    font-family: 'Quicksand', sans-serif;
    color: var(--ink);
    position: relative;
  }
  .card {
    position: absolute;
    left: 250px;
    width: 700px;
    height: 400px;
    box-shadow: 0 6px 18px rgba(0,0,0,0.18);
  }
  .card-front { top: 60px; background: var(--card-white); }
  .card-back { top: 540px; background: var(--card-black); }

  .accent-rule {
    position: absolute;
    left: 100px;
    width: 3px;
    background: var(--red);
  }
  .accent-rule.top { top: 0; height: 105px; }
  .accent-rule.bottom { bottom: 0; height: 60px; }

  .holder-name {
    position: absolute;
    left: 90px;
    top: 125px;
    font-size: 40px;
    font-weight: 500;
    letter-spacing: 0.5px;
    white-space: nowrap;
  }
  .holder-name .surname { color: var(--red); }
  .holder-email {
    position: absolute;
    left: 92px;
    top: 178px;
    font-size: 15px;
  }

  .showroom {
    position: absolute;
    font-size: 15px;
    line-height: 21px;
    letter-spacing: 0.4px;
    white-space: nowrap;
  }
  .showroom.gdl { left: 62px; top: 245px; }
  .showroom.cdmx { left: 330px; top: 275px; }
  .line { display: flex; align-items: center; gap: 8px; }
  .line.indent { padding-left: 24px; }
  .icon { width: 16px; height: 16px; flex: none; }

  .brand {
    position: absolute;
    left: 0; right: 0;
    top: 150px;
    text-align: center;
    color: var(--light);
  }
  .brand-name {
    font-size: 58px;
    font-weight: 400;
    letter-spacing: 10px;
  }
  .legal-name {
    margin-top: 14px;
    font-size: 13px;
    letter-spacing: 4px;
    text-transform: uppercase;
  }
</style>
</head>
<body>
  <section class="card card-front">
    <div class="accent-rule top"></div>
    <div class="accent-rule bottom"></div>

    <h1 class="holder-name">Lucia <span class="surname">Alcor Menteri</span></h1>
    <p class="holder-email">lucia@pietro.com.mx</p>

    <div class="showroom gdl">
      <div class="line">
        <svg class="icon" viewBox="0 0 16 16"><rect width="16" height="16" rx="2" fill="var(--red)"/><path d="M3 8 L8 3.5 L13 8 M5 7.5 V12.5 H11 V7.5" fill="none" stroke="#fff" stroke-width="1.5"/></svg>
        Ceramista 1830 Col. Piedralinda
      </div>
      <div class="line indent">Guadalajara, Jal</div>
      <div class="line">
        <svg class="icon" viewBox="0 0 16 16"><rect width="16" height="16" rx="2" fill="var(--red)"/><rect x="3.5" y="6" width="9" height="6.5" rx="1" fill="#fff"/><path d="M3.5 5 Q8 2 12.5 5" fill="none" stroke="#fff" stroke-width="1.5"/></svg>
        (33) 3000 1245
      </div>
      <div class="line">
        <svg class="icon" viewBox="0 0 16 16"><rect width="16" height="16" rx="2" fill="var(--red)"/><rect x="5" y="2.5" width="6" height="11" rx="1" fill="none" stroke="#fff" stroke-width="1.4"/></svg>
        (33) 1000 7788
      </div>
    </div>

    <div class="showroom cdmx">
      <div class="line">
        <svg class="icon" viewBox="0 0 16 16"><rect width="16" height="16" rx="2" fill="var(--red)"/><path d="M3 8 L8 3.5 L13 8 M5 7.5 V12.5 H11 V7.5" fill="none" stroke="#fff" stroke-width="1.5"/></svg>
        Calle Marmolera 245 B
      </div>
      <div class="line indent">Col. Loma Serena, Del.Sierra Norte</div>
      <div class="line indent">Mexico&nbsp; D.F.</div>
      <div class="line">
        <svg class="icon" viewBox="0 0 16 16"><rect width="16" height="16" rx="2" fill="var(--red)"/><rect x="3.5" y="6" width="9" height="6.5" rx="1" fill="#fff"/><path d="M3.5 5 Q8 2 12.5 5" fill="none" stroke="#fff" stroke-width="1.5"/></svg>
        (55) 5000 3142
      </div>
    </div>
  </section>

  <section class="card card-back">
    <div class="brand">
      <div class="brand-name">PIETRO</div>
      <div class="legal-name">Grande Volta SA de CV</div>
    </div>
  </section>
</body>
</html>
```